Lanterns Over Winter / Tidewater Song Guild / Flyer and Post Card Needed

Tidewater Song Guild is an acapella chorus in Sacramento, CA. We need an 8 1/2 x 11 flyer and a 5 x 7 postcard designed for our show. We are looking for a holiday-inspired marketing flyer to advertise the date and time of the show, venue, and special guests. Ticket prices should also be included on the flyer. We look forward to your submissions.

Target Market(s)

Family oriented, Live Music, Holiday Concert

Requirements
Must have
• Chorus Name and Logo (Provided) / Show title / Venue Name and address / website address / date and times of the show / ticket prices
Nice to have
• Holiday theme
Should not have
• Religious imagery

```html
<!DOCTYPE html>
<html lang="en">
<head>
<meta charset="utf-8">
<title>Lanterns Over Winter – Tidewater Song Guild</title>
<link href="https://fonts.googleapis.com/css2?family=Montserrat:wght@500;600;700;800&display=swap" rel="stylesheet">
<style>
  :root {
    --backdrop: #5e5e5e;
    --purple: #6a1fa8;
    --blue: #2f4eb0;
    --paper: #f3f3f4;
    --ink: #1d1d22;
    --white: #ffffff;
  }
  * { box-sizing: border-box; margin: 0; padding: 0; }
  html, body { width: 1200px; height: 900px; overflow: hidden; }
  body {
    background: var(--backdrop);
    font-family: "Montserrat", sans-serif;
    color: var(--ink);
    position: relative;
  }
  .postcard {
    position: absolute;
    left: 50px; top: 105px;
    width: 1100px; height: 690px;
    background: var(--paper);
    overflow: hidden;
  }
  .hero-photo {
    position: absolute; left: 0; top: 0;
    width: 100%; height: 300px;
    background:
      radial-gradient(ellipse at 65% 70%, rgba(120,80,130,.55), transparent 60%),
      linear-gradient(90deg, #3a2420 0%, #4c302a 30%, #2c1c19 60%, #3d2722 100%);
  }
  .chorus-name {
    position: absolute; left: 330px; top: 125px;
    font-weight: 600; font-size: 30px; color: var(--white);
    letter-spacing: .5px; white-space: nowrap;
  }
  .title-band {
    position: absolute; left: 0; top: 300px;
    width: 100%; height: 60px;
    background: var(--purple);
    display: flex; align-items: center; justify-content: center;
  }
  .show-title {
    font-weight: 800; font-size: 38px; color: var(--white);
    text-transform: uppercase; letter-spacing: 1px; white-space: nowrap;
  }
  .pill {
    display: inline-block;
    background: var(--blue); color: var(--white);
    font-weight: 800; font-size: 16px; text-transform: uppercase;
    padding: 3px 12px; border-radius: 9px; line-height: 20px;
  }
  .venue { position: absolute; left: 100px; top: 374px; width: 440px; }
  .venue-name { font-weight: 700; font-size: 18px; margin-top: 6px; white-space: nowrap; }
  .venue-address { font-weight: 500; font-size: 17px; margin-top: 2px; white-space: nowrap; }
  .info-table {
    border: 2px solid var(--blue);
    border-radius: 10px; overflow: hidden;
    background: var(--white);
  }
  .info-table .table-head {
    background: var(--blue); color: var(--white);
    font-weight: 800; font-size: 19px; text-transform: uppercase;
    text-align: center; padding: 4px 0; letter-spacing: .5px; line-height: 24px;
  }
  .ticket-table { position: absolute; left: 100px; top: 466px; width: 400px; }
  .ticket-row { display: flex; border-top: 1.5px solid var(--blue); font-size: 16px; line-height: 24px; white-space: nowrap; }
  .ticket-price { width: 120px; font-weight: 700; padding: 2px 12px; border-right: 1.5px solid var(--blue); }
  .ticket-type { padding: 2px 14px; font-weight: 500; }
  .schedule { position: absolute; left: 565px; top: 372px; }
  .schedule-line { display: flex; align-items: center; gap: 10px; margin-bottom: 5px; }
  .schedule-text { font-weight: 700; font-size: 18px; white-space: nowrap; }
  .guest-name {
    position: absolute; left: 880px; top: 384px;
    font-weight: 600; font-size: 17px; color: var(--ink); white-space: nowrap;
  }
  .guest-table { position: absolute; left: 565px; top: 474px; width: 500px; }
  .guest-feature { padding: 5px 14px; font-weight: 700; font-size: 15px; line-height: 22px; white-space: nowrap; }
  .guest-row { display: flex; border-top: 1.5px solid var(--blue); font-size: 15px; font-weight: 500; line-height: 22px; white-space: nowrap; }
  .guest-row span { flex: 1; padding: 5px 14px; }
  .guest-row span + span { border-left: 1.5px solid var(--blue); }
  .footer-band {
    position: absolute; left: 0; bottom: 0;
    width: 100%; height: 60px;
    background: var(--purple);
    display: flex; align-items: center; justify-content: center;
    padding-left: 260px;
  }
  .website { color: var(--white); font-weight: 600; font-size: 22px; letter-spacing: 2px; white-space: nowrap; }
</style>
</head>
<body>
  <article class="postcard">
    <div class="hero-photo" role="img" aria-label="Photo of the chorus on stage in dark suits, arms raised, in front of a brown curtain"></div>
    <div class="chorus-name">Tidewater Song Guild</div>

    <div class="title-band"><h1 class="show-title">Lanterns Over Winter</h1></div>

    <section class="venue">
      <span class="pill">Venue:</span>
      <p class="venue-name">Harborlight Performing Arts Hall</p>
      <p class="venue-address">2150 Beacon Lane, Riverton, CA 95800</p>
    </section>

    <section class="info-table ticket-table">
      <div class="table-head">Ticket Prices:</div>
      <div class="ticket-row"><span class="ticket-price">$30.00</span><span class="ticket-type">VIP Seating</span></div>
      <div class="ticket-row"><span class="ticket-price">$20.00</span><span class="ticket-type">General Admission</span></div>
      <div class="ticket-row"><span class="ticket-price">$12.00</span><span class="ticket-type">Student / Senior</span></div>
    </section>

    <section class="schedule">
      <div class="schedule-line"><span class="pill">Date:</span></div>
      <div class="schedule-line"><span class="schedule-text">Saturday, December 4, 2021</span></div>
      <div class="schedule-line"><span class="pill">Times:</span><span class="schedule-text">2:00 pm / 8:00 pm</span></div>
    </section>

    <div class="guest-name">Silver Chord Quartet</div>

    <section class="info-table guest-table">
      <div class="table-head">Special Guests:</div>
      <div class="guest-feature">Silver Chord Quartet – 2011 Western Region Champions</div>
      <div class="guest-row"><span>Northgate High School</span><span>Cedar Ridge High School</span></div>
    </section>

    <footer class="footer-band"><span class="website">www.tidewatersongguild.org</span></footer>
  </article>
</body>
</html>
```